Flalzflyer-Design (Folder)
Da für uns neben einem guten Design ein angenehmer und konstruktiver Dialog sowie Verlässlichkeit von hoher Bedeutung ist, sind wir sehr froh auf dieser Plattform auf "brightpixel" gestoßen zu sein. Wir sagen ganz herzlich DANKE!!
Zielgruppe
Zielgruppe im Bereich der Vermietung sind Alleinreisende oder als Paar verreisende Natur- und Nordsee verbundene Feriengäste (ü30) mit dem Urlaubsziel 'Sylt', welche eine persönlich und mit besonderem Schick eingerichtet Ferienwohnung/Ferienapartment in zentraler Lage in Westerland suchen und die es als positiven bzw. interessanten Aspekt sehen, dass die Ferienwohnungen direkt von uns Insulaner angeboten werden und wir als Sylter Familie ebenfalls Vor-Ort mit dem Urlaubern unter dem selben Dach leben (wenn auch nicht in der derselben Wohnung ;) ), ganz gemäß unserem Slogan 'Küstenferien Tür an Tür mit Gastgebern'
Aufgabenstellung
Es soll ein Falzflyer (Folder) mit Wickelfalz (siehe ggf. https://www.druckhafen-muster.de/werbemittel/folder.html) designed werden (4/4-farbig Euroskala). Bestehend aus einem Papier Format DIN A4 mit zwei Falzen, sodass sich bei Berücksichtigung von Vor- u. Rückseite 6 Seiten ergeben. Die wesentlichen Texte/Inhalte/Informationen, finden sich hier: https://www.urlaubsquartier-beispiel.de/481527/ . Neben dem Ferienapartment 'Möwe' w ird von uns die Ferienwohnung 'Brolke' (friesisch für Seestern) angeboten, ebenfalls im Dünenhain Quartier HOUSE (EST. 2017).
Preisangaben können unberücksichtigt beliben, da sie dem Folder später über eine gesondere Einlage beigelegt werden sollen.
Im Rahmen des Dateiupload bei entwurfsportal werden nur einige der möglichen Fotos bereitgestellt. Sie sollen als Auswahlmöglichkeit dienen. Welche der Fotos Verwendung finden oder nach weiteren nachgefragt wird, soll in Abhängigkeit mit dem Gesamtdesign stehen und zunächst von Ihnen entschieden werden, um ein möglichst ansprechenden und harmonischen Folder kreieren zu können.

```html
<!DOCTYPE html>
<html lang="de">
<head>
<meta charset="utf-8">
<title>Ferienzeit Dünenhain – Folder</title>
<link rel="stylesheet" href="https://fonts.googleapis.com/css2?family=Alegreya+Sans:wght@300;400;500;700&family=Alegreya+Sans+SC:wght@500&display=swap">
<style>
  :root {
    --paper: #ffffff;
    --sand: #bab2a3;
    --ink: #4d4a45;
    --olive: #7b7662;
    --quote: #a09c6e;
    --sky: #a9c3da;
    --white: #ffffff;
    --fold: #6f87a8;
    --photo-sea: linear-gradient(180deg, #8fa7c4 0%, #c9d3dd 40%, #bfb29b 62%, #a89a84 100%);
    --photo-room: linear-gradient(135deg, #d6d3cc 0%, #b9b4ad 45%, #3e3c3d 70%, #e8e6e2 100%);
    --photo-bowls: linear-gradient(135deg, #6f89b0 0%, #d9d4cb 55%, #44506a 100%);
    --photo-shelf: linear-gradient(135deg, #9a8f86 0%, #d9c9c0 45%, #8a5b6a 100%);
    --photo-bed: linear-gradient(135deg, #7b7875 0%, #d7d4cf 50%, #5b4f46 100%);
    --photo-bath: linear-gradient(160deg, #b8c96a 0%, #e9e8e2 50%, #8d8a84 100%);
    --plan: linear-gradient(180deg, #e4e0d8 0%, #d8d3ca 100%);
  }
  * { margin: 0; padding: 0; box-sizing: border-box; }
  html, body { width: 1200px; height: 840px; overflow: hidden; background: var(--paper); }
  body { font-family: "Alegreya Sans", "Gill Sans", sans-serif; color: var(--ink); }
  .folder { position: relative; width: 1200px; height: 840px; background: var(--paper); }

  .fold-line { position: absolute; top: 0; bottom: 0; width: 0; border-left: 1.5px dashed var(--fold); }
  .fold-line--one { left: 418px; }
  .fold-line--two { left: 800px; }

  .sand-panel { position: absolute; left: 420px; top: 20px; width: 760px; height: 799px; background: var(--sand); }

  .eyebrow { position: absolute; font-family: "Alegreya Sans", sans-serif; font-weight: 700; font-size: 13px; letter-spacing: 1.2px; text-transform: uppercase; }
  .eyebrow--cover { left: 21px; top: 46px; color: var(--olive); opacity: .85; }
  .eyebrow--apartment { left: 442px; top: 44px; color: var(--white); }
  .eyebrow--plan { left: 849px; top: 573px; color: var(--white); }

  .title { position: absolute; font-weight: 300; font-size: 50px; line-height: 1; }
  .title--cover { left: 62px; top: 60px; color: var(--olive); }
  .title--apartment { left: 606px; top: 60px; color: var(--white); }

  .photo { position: absolute; }
  .photo--beach { left: 40px; top: 170px; width: 330px; height: 237px; background: var(--photo-sea); }
  .photo--living { left: 455px; top: 99px; width: 315px; height: 231px; background: var(--photo-room); }
  .photo--bowls { left: 840px; top: 268px; width: 107px; height: 107px; background: var(--photo-bowls); }
  .photo--shelf { left: 966px; top: 268px; width: 193px; height: 194px; background: var(--photo-shelf); }
  .photo--bedroom { left: 442px; top: 604px; width: 181px; height: 182px; background: var(--photo-bed); }
  .photo--bath { left: 647px; top: 652px; width: 133px; height: 134px; background: var(--photo-bath); }
  .photo--plan { left: 846px; top: 604px; width: 295px; height: 181px; background: var(--plan); }

  .corners { position: absolute; overflow: visible; }
  .corners--beach { left: 28px; top: 158px; }
  .corners--living { left: 442px; top: 90px; }
  .corners--plan { left: 823px; top: 537px; }

  .pull-quote { position: absolute; left: 40px; top: 452px; width: 340px; font-family: "Alegreya Sans SC", sans-serif; font-weight: 500; font-size: 18px; letter-spacing: .8px; color: var(--quote); }

  .copy { position: absolute; font-size: 13.4px; line-height: 21px; }
  .copy--cover { left: 40px; top: 492px; width: 335px; color: var(--ink); }
  .copy--apartment { left: 442px; top: 360px; width: 335px; color: var(--white); }
  .copy--rooms { left: 839px; top: 95px; width: 300px; color: var(--white); }
</style>
</head>
<body>
<main class="folder">
  <div class="sand-panel"></div>
  <div class="fold-line fold-line--one"></div>
  <div class="fold-line fold-line--two"></div>

  <!-- Cover panel -->
  <section class="cover">
    <p class="eyebrow eyebrow--cover">Ferienzeit</p>
    <h1 class="title title--cover">Dünenhain</h1>
    <div class="photo photo--beach" role="img" aria-label="Foto: Sandstrand mit Spaziergängern unter blauem Himmel mit Wolken"></div>
    <svg class="corners corners--beach" width="354" height="261" viewBox="0 0 354 261" aria-hidden="true">
      <g fill="none" stroke="var(--sky)" stroke-width="12">
        <path d="M6 40 V6 H40"/><path d="M314 6 H348 V40"/>
        <path d="M6 221 V255 H40"/><path d="M314 255 H348 V221"/>
      </g>
    </svg>
    <h2 class="pull-quote">„Untia porerch illuptam eos maio.“</h2>
    <div class="copy copy--cover">
      <p>Is ad moluptatur rem arupta dolent. Tio iurem quia susam, qui comnis rescimendi sinullore denis ullaborerume illuptatur alistiatur molor antinverspe pos aut quam, sum reptat dis qui officip itaquibus que por aut et vernatis ne perrovid quodipsam quaerae. Porpos pero bla corumquia consequi te volorep tiumetur maio. Cipsandant.</p>
      <p>Icil este et, nonseque solent, am imagnisti tem autempor animporem quia volessitem num nis a proviti doluptae plaudignimi, sunt adio tem nulpa aut est ommos derios.</p>
      <p>Qui officip itaquibus que por aut et vernatis ne perrovid quodipsam quaerae. Porpos pero bla corumquia consequi te volorep tiumetur maio. Cipsandant.</p>
    </div>
  </section>

  <!-- Apartment panel -->
  <section class="apartment">
    <p class="eyebrow eyebrow--apartment">Apartment</p>
    <h2 class="title title--apartment">Möwe</h2>
    <div class="photo photo--living" role="img" aria-label="Foto: Wohnbereich mit dunklem Sofa, Kissen und kleinem blauen Tisch"></div>
    <svg class="corners corners--living" width="338" height="249" viewBox="0 0 338 249" aria-hidden="true">
      <g fill="none" stroke="var(--white)" stroke-width="10">
        <path d="M5 35 V5 H35"/><path d="M303 5 H333 V35"/>
        <path d="M5 214 V244 H35"/><path d="M303 244 H333 V214"/>
      </g>
    </svg>
    <div class="copy copy--apartment">
      <p>Wer Meer hat, braucht weniger, sagt man.</p>
      <p>Wir haben im Dünenhain Quartier House (est. 2017) dennoch im Vergleich zu vielen Apartments auf der Insel Sylt ein angenehmes „Mehr“ für einen schönen Aufenthalt:</p>
      <p>Die Zimmer persönlich und mit Geschick gestaltet, zeitgemäße Wohneinrichtung, modernes ebenerdiges Duschbad, hochwertige Pantryküche, Smart-TV, Wlan, ansprechendes und vollständiges Geschirr, Außenbereich sowie der persönlichen Nähe zu uns Insulanern.</p>
    </div>
    <div class="photo photo--bedroom" role="img" aria-label="Foto: Schlafzimmer mit Einzelbett und Holzregal"></div>
    <div class="photo photo--bath" role="img" aria-label="Foto: Duschbad mit Waschbecken und grüner Wand"></div>
  </section>

  <!-- Rooms panel -->
  <section class="rooms">
    <div class="copy copy--rooms">
      <p>Das Apartment eignet sich für einen längeren Urlaub besonders für 1 Person.</p>
      <p>Es steht ein Einzelbett im kleinen Schlafzimmer zur Verfügung. Für einen Aufenthalt von einigen Tagen haben 2 Personen ebenfalls eine passend schöne Unterkunft (Schlafmöglichkeit auf komfortablen Schlafsofa mit Lattenrost).</p>
    </div>
    <div class="photo photo--bowls" role="img" aria-label="Foto: blau-weiße Schalen auf dem Tisch"></div>
    <div class="photo photo--shelf" role="img" aria-label="Foto: Wandregal mit Deko-Schriftzug und Vogelfigur"></div>
    <svg class="corners corners--plan" width="338" height="247" viewBox="0 0 338 247" aria-hidden="true">
      <g fill="none" stroke="var(--white)" stroke-width="10">
        <path d="M5 35 V5 H35"/><path d="M303 5 H333 V35"/>
        <path d="M5 212 V242 H35"/><path d="M303 242 H333 V212"/>
      </g>
    </svg>
    <p class="eyebrow eyebrow--plan">Grundriss</p>
    <div class="photo photo--plan" role="img" aria-label="Grundriss des Apartments mit Schlafzimmer, Wohnbereich, Bad und Außenbereich"></div>
  </section>
</main>
</body>
</html>
```